Forensic Psychology and Polygraph Needs Clever Catchy Logo

There's a massive trade show coming up and we are looking to debut a new, clever logo for our business cards. We are a private practice that offers psychological evaluations, therapeutic counseling, and polygraphing. Our website is ketvorin.com (to get a better idea of the color scheme) and instead of the nature/cuddly image that other psychology organizations like to go for, we are interested in cultivating a business, strength, and professional image.
Attached are some popular logos and designs to get those creative juices flowing! I would like to avoid the brain/psi logo as this has been to death so bonus points definitely for originality.
Target Market(s)
governmental agencies, third party mental health providers, individual private pay clients
Industry/Entity Type
Mental Health
Contact Information for Business Card
One one side will be the logo and company name while on the back will be contact information and provider details (name, position, etc)
Look and feel

```html
<!DOCTYPE html>
<html lang="en">
<head>
<meta charset="UTF-8">
<title>Ketvorin &amp; Associates — Business Cards</title>
<link href="https://fonts.googleapis.com/css2?family=Questrial&family=Open+Sans:wght@400;600;700&display=swap" rel="stylesheet">
<style>
  :root {
    --teal: #3fa6a8;
    --teal-light: #7cc6c6;
    --teal-dark: #2f8e90;
    --grey-text: #6f7072;
    --grey-light: #9a9b9d;
    --card: #ffffff;
    --backdrop: #e9e7e3;
  }
  * { box-sizing: border-box; margin: 0; padding: 0; }
  html, body {
    width: 1200px; height: 800px; overflow: hidden;
    background: var(--backdrop);
  }
  .stage {
    position: relative; width: 1200px; height: 800px;
    display: flex; align-items: center; justify-content: center; gap: 44px;
  }
  .card {
    position: relative; width: 540px; height: 309px;
    background: var(--card);
    box-shadow: 0 6px 22px rgba(0,0,0,0.14);
    overflow: hidden;
  }

  /* Back: contact side */
  .provider {
    position: absolute; left: 34px; top: 34px;
    padding-left: 14px; border-left: 6px solid var(--teal);
  }
  .provider-name {
    font-family: "Open Sans", sans-serif; font-weight: 700;
    font-size: 22px; color: var(--grey-text); line-height: 1.1;
  }
  .provider-role {
    font-family: "Open Sans", sans-serif; font-weight: 400;
    font-size: 14px; color: var(--teal); margin-top: 2px;
  }
  .contacts {
    position: absolute; left: 34px; bottom: 66px;
    list-style: none;
  }
  .contacts li {
    display: flex; align-items: center; gap: 10px;
    font-family: "Open Sans", sans-serif; font-size: 13px;
    color: var(--grey-text); margin-top: 6px;
  }
  .contacts svg { width: 16px; height: 16px; flex: none; }
  .band {
    position: absolute; left: 0; right: 0; bottom: 0; height: 48px;
  }

  /* Logo lockup */
  .lockup {
    position: absolute; display: flex; align-items: center; gap: 10px;
  }
  .lockup-mark { background: var(--teal); flex: none; }
  .lockup-name {
    font-family: "Questrial", sans-serif; color: var(--grey-text);
    line-height: 1; white-space: nowrap;
  }
  .lockup-tagline {
    font-family: "Open Sans", sans-serif; color: var(--teal);
    letter-spacing: 0.22em; text-transform: uppercase; margin-top: 4px;
    white-space: nowrap;
  }
  .card-back .lockup { right: 30px; bottom: 72px; }
  .card-back .lockup-mark { width: 18px; height: 18px; }
  .card-back .lockup-name { font-size: 22px; }
  .card-back .lockup-tagline { font-size: 8px; }

  .card-front .lockup { left: 70px; bottom: 56px; }
  .card-front .lockup-mark { width: 24px; height: 24px; }
  .card-front .lockup-name { font-size: 32px; }
  .card-front .lockup-tagline { font-size: 10.5px; }
</style>
</head>
<body>
<main class="stage">

  <section class="card card-back" aria-label="Business card, contact side">
    <div class="provider">
      <p class="provider-name">Your Name</p>
      <p class="provider-role">Partner</p>
    </div>

    <ul class="contacts">
      <li>
        <svg viewBox="0 0 16 16" aria-hidden="true"><path fill="#3fa6a8" d="M2 5c0-1.5 2.5-2.5 6-2.5S14 3.5 14 5v1.3h-3V5H5v1.3H2zM4 7h8l1.5 6.5h-11z"/><circle cx="8" cy="10.2" r="1.6" fill="#fff"/></svg>
        <span>000 000 0000</span>
      </li>
      <li>
        <svg viewBox="0 0 16 16" aria-hidden="true"><rect x="1.5" y="3.5" width="13" height="9" fill="#3fa6a8"/><path d="M1.5 3.5L8 9l6.5-5.5" fill="none" stroke="#fff" stroke-width="1.2"/></svg>
        <span>youremail@xyz.com</span>
      </li>
      <li>
        <svg viewBox="0 0 16 16" aria-hidden="true"><g fill="none" stroke="#3fa6a8" stroke-width="1.3"><circle cx="8" cy="8" r="6.2"/><ellipse cx="8" cy="8" rx="2.6" ry="6.2"/><path d="M1.8 8h12.4M3 4.6h10M3 11.4h10"/></g></svg>
        <span>ketvorin.com</span>
      </li>
    </ul>

    <div class="lockup">
      <span class="lockup-mark"></span>
      <div>
        <p class="lockup-name">Ketvorin &amp; Associates</p>
        <p class="lockup-tagline">Psychological Services, PLLC</p>
      </div>
    </div>

    <svg class="band" viewBox="0 0 540 48" preserveAspectRatio="none" aria-hidden="true">
      <rect x="0" y="0" width="540" height="48" fill="#7cc6c6"/>
      <polygon points="0,14 540,6 540,48 0,48" fill="#3fa6a8"/>
    </svg>
  </section>

  <section class="card card-front" aria-label="Business card, logo side">
    <div class="lockup">
      <span class="lockup-mark"></span>
      <div>
        <p class="lockup-name">Ketvorin &amp; Associates</p>
        <p class="lockup-tagline">Psychological Services, PLLC</p>
      </div>
    </div>
  </section>

</main>
</body>
</html>
```